Skyreach Northern Flights
Private Charters
Skyreach Northern Flights  - Aviation
Creative Brief
Cutting-Edge
Tamara Holbrook
Business Development
5127 N. Darrow, Suite 240 Scottsdale, AZ 85254
tholbrook@skyreachnorthernflights.example
www.skyreachnorthernflights.example

```html
<!DOCTYPE html>
<html lang="en">
<head>
<meta charset="utf-8">
<title>Skyreach Northern Flights — Stationery Suite</title>
<link href="https://fonts.googleapis.com/css2?family=Cinzel:wght@400;600&family=Oswald:wght@500&display=swap" rel="stylesheet">
<style>
:root{
  --maroon:#7a1d1d;
  --maroon-dark:#5e1313;
  --paper-grey:#e4e2e2;
  --line:#c9c5c5;
  --ink:#3a3a3a;
  --label:#111;
}
*{box-sizing:border-box;margin:0;padding:0}
html,body{width:1200px;height:871px;overflow:hidden;background:#fff}
.canvas{position:relative;width:1200px;height:871px;background:#fff;font-family:"Cinzel",serif;color:var(--ink)}
.piece{position:absolute;background:linear-gradient(160deg,#fbfbfb,var(--paper-grey));box-shadow:1px 2px 4px rgba(0,0,0,.35);overflow:hidden}
.label{position:absolute;font-family:"Oswald",sans-serif;font-weight:500;font-size:19px;color:var(--label);letter-spacing:.5px;white-space:nowrap;z-index:5}
.label.vertical{transform:rotate(-90deg);transform-origin:left top}
.label.vertical-right{transform:rotate(90deg);transform-origin:left top}
.wordmark{position:absolute;display:flex;align-items:center;justify-content:center;gap:6px;color:var(--maroon);font-family:"Cinzel",serif;font-weight:600;letter-spacing:1px;line-height:1.1;text-align:center}
.wordmark .dot{width:7px;height:7px;border-radius:50%;background:var(--maroon);flex:none}
.wordmark.light{color:#fff}
.wordmark.light .dot{background:#fff}
.contact{position:absolute;font-family:"Cinzel",serif;font-size:7px;line-height:1.4;color:var(--ink);white-space:nowrap}
.contact.light{color:#fff}
.web{position:absolute;font-family:"Cinzel",serif;font-size:7px;color:var(--ink);white-space:nowrap;text-align:center}
.band{position:absolute;background:var(--maroon)}
.rule{position:absolute;height:1px;background:var(--line)}
.form-field{position:absolute;font-size:9px;color:var(--ink)}
.tag{position:absolute;width:96px;height:96px;filter:drop-shadow(1px 2px 3px rgba(0,0,0,.35))}
.tag-face{position:absolute;inset:0;clip-path:polygon(50% 0,100% 50%,50% 100%,0 50%)}
</style>
</head>
<body>
<div class="canvas">

  <!-- labels -->
  <div class="label vertical" style="left:18px;top:152px">BIZ CARD</div>
  <div class="label" style="left:92px;top:0">FRONT</div>
  <div class="label" style="left:250px;top:30px">BACK</div>
  <div class="label" style="left:514px;top:2px">ENVELOPE BACK</div>
  <div class="label" style="left:930px;top:8px">LETTER HEAD</div>
  <div class="label vertical" style="left:18px;top:420px">ENVELOPE FRONT</div>
  <div class="label" style="left:726px;top:376px">TAGS</div>
  <div class="label" style="left:696px;top:552px">BADGE</div>
  <div class="label vertical" style="left:18px;top:852px">PRESENTATION FOLDER</div>
  <div class="label" style="left:500px;top:828px">BOOKMARK</div>
  <div class="label" style="left:628px;top:836px">CD/DVD COVER FRONT</div>
  <div class="label vertical-right" style="left:1196px;top:566px">CD/DVD INSIDE FLAP</div>

  <!-- business card front -->
  <section class="piece biz-card-front" style="left:48px;top:26px;width:142px;height:78px">
    <div class="contact" style="left:6px;top:5px;font-size:6px"><b>TAMARA HOLBROOK</b><br>Business Development</div>
    <div class="wordmark" style="left:6px;top:32px;width:110px;font-size:7.5px"><span class="dot"></span><span>Skyreach Northern Flights</span></div>
    <div class="contact" style="left:62px;top:54px;font-size:4.8px;line-height:1.3">PHONE · 480-555-0142<br>CELL · 480-555-0187<br>FAX · 480-555-0163</div>
    <div class="band" style="right:0;top:0;width:20px;height:78px;border-radius:0 0 0 22px"></div>
  </section>

  <!-- business card back -->
  <section class="piece biz-card-back" style="left:206px;top:56px;width:152px;height:56px">
    <div class="wordmark" style="left:8px;top:14px;width:136px;font-size:8px"><span class="dot"></span><span>Skyreach Northern Flights</span></div>
    <div class="web" style="left:0;top:40px;width:152px;font-size:4.8px">www.skyreachnorthernflights.example</div>
  </section>

  <!-- envelope back -->
  <section class="piece envelope-back" style="left:384px;top:28px;width:420px;height:240px">
    <svg width="420" height="240" style="position:absolute;left:0;top:0">
      <path d="M0 0H420V40L210 130L0 40Z" fill="var(--maroon)"/>
      <path d="M0 240L185 148M420 240L235 148" stroke="var(--line)" fill="none"/>
    </svg>
    <div class="wordmark light" style="left:130px;top:54px;width:160px;font-size:10px"><span>Skyreach Northern Flights</span></div>
    <div class="web" style="left:0;top:214px;width:420px">www.skyreachnorthernflights.example</div>
  </section>

  <!-- envelope front -->
  <section class="piece envelope-front" style="left:48px;top:112px;width:392px;height:296px;z-index:2">
    <div class="wordmark" style="left:14px;top:44px;width:170px;font-size:12px;justify-content:flex-start"><span class="dot"></span><span>Skyreach Northern Flights</span></div>
    <div class="rule" style="left:16px;top:92px;width:330px;background:linear-gradient(90deg,var(--maroon),transparent)"></div>
    <div class="contact" style="left:150px;top:226px">5127 N. DARROW, SUITE 240<br>SCOTTSDALE, AZ 85254<br>PHONE · 480-555-0142<br>CELL · 480-555-0187<br>FAX · 480-555-0163</div>
    <div class="band" style="right:0;top:0;width:34px;height:296px;border-radius:0 0 0 34px"></div>
  </section>

  <!-- letterhead -->
  <section class="piece letterhead" style="left:810px;top:40px;width:354px;height:474px">
    <div class="wordmark" style="left:20px;top:22px;width:120px;font-size:11px;justify-content:flex-start"><span class="dot"></span><span>Skyreach Northern Flights</span></div>
    <div class="form-field" style="left:22px;top:96px">TO:</div>
    <div class="form-field" style="left:240px;top:96px">DATE:</div>
    <div class="form-field" style="left:22px;top:124px">FROM:</div>
    <div class="form-field" style="left:22px;top:152px">SUBJECT:</div>
    <div class="rule" style="left:20px;top:176px;width:314px"></div>
    <div class="contact" style="left:22px;top:414px;font-size:6px">5127 N. DARROW, SUITE 240<br>SCOTTSDALE, AZ 85254</div>
    <div class="contact" style="left:22px;top:434px;font-size:6px">PHONE · 480-555-0142 · FAX · 480-555-0163</div>
    <div class="band" style="right:0;bottom:0;width:44px;height:474px;border-radius:0 0 0 44px"></div>
  </section>

  <!-- tags -->
  <section class="tag" style="left:499px;top:288px">
    <div class="tag-face" style="background:var(--maroon)"></div>
    <div class="wordmark light" style="left:18px;top:36px;width:60px;font-size:6.5px"><span>Skyreach Northern Flights</span></div>
  </section>
  <section class="tag" style="left:624px;top:288px">
    <div class="tag-face" style="background:linear-gradient(160deg,#fbfbfb,var(--paper-grey))"></div>
    <div class="wordmark" style="left:18px;top:36px;width:60px;font-size:6.5px"><span>Skyreach Northern Flights</span></div>
  </section>

  <!-- badge -->
  <section class="badge" style="position:absolute;left:530px;top:394px;width:150px;height:150px;border-radius:50%;background:radial-gradient(circle at 40% 30%,#b04040,var(--maroon) 55%,var(--maroon-dark));box-shadow:2px 3px 6px rgba(0,0,0,.4)">
    <div class="wordmark light" style="left:20px;top:60px;width:110px;font-size:11px"><span>Skyreach Northern Flights</span></div>
  </section>

  <!-- presentation folder -->
  <section class="piece folder-cover" style="left:48px;top:444px;width:216px;height:408px;background:var(--maroon)">
    <div class="wordmark light" style="left:16px;top:150px;width:184px;font-size:12px"><span>Skyreach Northern Flights</span></div>
    <div class="contact light" style="left:28px;top:222px">5127 N. DARROW, SUITE 240<br>SCOTTSDALE, AZ 85254<br><br>PHONE · 480-555-0142<br>CELL · 480-555-0187<br>FAX · 480-555-0163</div>
  </section>
  <section class="piece folder-inside" style="left:276px;top:444px;width:216px;height:408px">
    <div class="wordmark" style="left:20px;top:40px;width:176px;font-size:10px"><span>Skyreach Northern Flights</span></div>
    <div class="band" style="left:0;bottom:0;width:216px;height:60px;border-radius:80px 0 0 0"></div>
  </section>

  <!-- bookmark -->
  <section class="piece bookmark" style="left:511px;top:560px;width:78px;height:256px;background:linear-gradient(180deg,var(--maroon),#f1eeee 45%)">
    <div class="wordmark" style="left:4px;top:128px;width:70px;font-size:7.5px"><span>Skyreach Northern Flights</span></div>
    <div class="web" style="left:0;top:232px;width:78px;font-size:5px;line-height:1.3">www.skyreachnorthern<br>flights.example</div>
  </section>

  <!-- cd cover front -->
  <section class="piece cd-cover" style="left:619px;top:566px;width:190px;height:250px">
    <div class="web" style="left:0;top:14px;width:190px;font-size:5.5px">www.skyreachnorthernflights.example</div>
    <div class="wordmark" style="left:14px;top:112px;width:162px;font-size:10px"><span class="dot"></span><span>Skyreach Northern Flights</span></div>
    <div class="band" style="left:0;bottom:0;width:190px;height:36px"></div>
  </section>

  <!-- cd inside flap -->
  <section class="piece cd-inside" style="left:822px;top:566px;width:320px;height:250px">
    <div class="band" style="left:0;bottom:0;width:320px;height:50px"></div>
    <div style="position:absolute;left:110px;top:10px;width:200px;height:200px;border-radius:50%;background:radial-gradient(circle,#fff 10%,#d8d6d6 11%,#f6f6f6 14%,#ececec 60%,#dcdada);box-shadow:1px 2px 5px rgba(0,0,0,.35)"></div>
    <div class="wordmark" style="left:150px;top:140px;width:120px;font-size:8px"><span>Skyreach Northern Flights</span></div>
  </section>

</div>
</body>
</html>
```